Web application design for investigative software

ThreadKove is an investigation web application that would organize, create visualizations and allow collaboration. It’s available to anyone and can be used by students, historians, watchdog groups, civic hackers, investigative reporters, mystery enthusiasts, authors, even conspiracy theorists.

We are looking for two related pages. The first, a splash, or front, page and the second a ‘template’ for the web application. They should both be styled the same. The only restriction is that the logo is set.

The design should also be modern and visually well organized — employing a combination of visual devices and info graphics. Keep it light and not too heavy but strong/ professional. Do not be influenced by the current colors of threadkove.example, though the colors should be compatible with the logo..

The pages should be compatible with bootstrap, mostly for it’s JS and component functionality. It can be advised by the designer that a subset of bootstrap be used.

The splash page.
Something along the lines of (though not a copy of) :
https://www.brimloft.example/advertise
http://www.palvornhosting.example/
http://www.murkelsoft.example/
http://www.vontasky.example/

I have a very rough wire frame ish html file uploaded. Use a a guide, but alternate ideas are encouraged.

The application page should have some sort of bar for at the top for system level links a header and a footer. A vertical column to the left between the header and footer for ads, though this will be dynamic as a user can pay out of seeing adds. All dynamic actions will be made by the developers at ThreadKove.

WARNING. Please do not submit pre-made templates from some template website. We can do that ourselves for free.

This project will deliver CODE. HTML, CSS and supporting graphics and files.

```html
<!DOCTYPE html>
<html lang="en">
<head>
<meta charset="utf-8">
<title>ThreadKove – Track, Relate, Investigate, Solve</title>
<link rel="stylesheet" href="https://fonts.googleapis.com/css2?family=Open+Sans:wght@300;400;600;700&display=swap">
<style>
:root{
  --red:#e8392b;
  --red-deep:#c9140c;
  --red-soft:#f25a45;
  --ink:#333333;
  --text:#5a5a5a;
  --muted:#7a7a7a;
  --band:#f3f3f3;
  --dark-btn:#3f3f3f;
  --footer:#3c3c3c;
  --white:#ffffff;
}
*{margin:0;padding:0;box-sizing:border-box}
html,body{width:701px;height:1200px;overflow:hidden;background:var(--white)}
body{font-family:"Open Sans",Arial,sans-serif;color:var(--text);position:relative}
.abs{position:absolute}

/* header */
.site-header{position:absolute;left:0;top:0;width:701px;height:65px;background:var(--white);border-bottom:1px solid #e6e6e6}
.brand{position:absolute;left:44px;top:20px;display:flex;align-items:center;gap:6px}
.brand-dot{width:22px;height:22px;border-radius:50%;background:var(--red)}
.brand-name{font-size:17px;font-weight:600;color:var(--red);letter-spacing:-.2px}
.main-nav{position:absolute;right:43px;top:34px;display:flex;gap:19px;font-size:10px}
.main-nav a{color:#555;text-decoration:none}
.main-nav a.accent{color:var(--red)}

/* hero */
.hero{position:absolute;left:0;top:65px;width:701px;height:285px;background:linear-gradient(135deg,#e4e1dc 0%,#c9b9a6 40%,#8a7b6c 70%,#d88a45 100%)}
.hero-caption{position:absolute;left:146px;top:161px;width:409px;height:56px;background:rgba(25,25,25,.82);text-align:center;color:var(--white)}
.hero-caption h1{font-weight:400;font-size:28px;line-height:32px;margin-top:1px}
.hero-caption h1 span{color:var(--red-soft)}
.hero-caption p{font-size:17px;line-height:20px}
.hero-caption p strong{color:var(--red-soft);font-weight:600}
.slider-dots{position:absolute;left:322px;top:253px;display:flex;gap:5px}
.slider-dots i{width:11px;height:11px;border-radius:50%;background:var(--white)}
.slider-dots i.on{background:var(--red)}

/* intro */
.intro{position:absolute;left:43px;top:368px;width:615px;text-align:center}
.section-title{font-weight:400;font-size:17.5px;color:var(--red);line-height:24px}
.body-copy{font-size:7.4px;line-height:12px;color:var(--text)}
.intro .section-title{margin-bottom:10px}
.intro .body-copy + .body-copy{margin-top:3px}

/* features */
.features{position:absolute;left:0;top:508px;width:701px;height:206px;background:repeating-linear-gradient(45deg,#f4f4f4 0 2px,#ececec 2px 4px)}
.feature-card{position:absolute;top:13px;width:193px;height:177px;background:radial-gradient(ellipse at 50% 20%,var(--red-soft) 0%,var(--red) 45%,var(--red-deep) 100%);text-align:center;color:var(--white)}
.feature-card svg{position:absolute;left:50%;transform:translateX(-50%);top:14px}
.feature-card h2{position:absolute;left:0;right:0;top:81px;font-weight:400;font-size:16px}
.feature-card p{position:absolute;left:16px;right:16px;top:107px;font-size:7.4px;line-height:12.5px}
.feature-card .learn{position:absolute;left:0;right:0;top:151px;font-size:7.4px;font-weight:600;letter-spacing:.2px}

/* how */
.how-title{position:absolute;left:43px;top:732px}
.how-copy{position:absolute;left:43px;top:764px;width:347px}
.btn{position:absolute;height:21px;background:var(--dark-btn);color:var(--white);font-size:7.6px;font-weight:600;display:flex;align-items:center;justify-content:center;border-radius:2px}
.photo{position:absolute}

/* get */
.get-band{position:absolute;left:0;top:892px;width:701px;height:178px;background:var(--band)}
.get-title{position:absolute;right:43px;top:906px;text-align:right}
.get-copy{position:absolute;right:43px;top:936px;width:405px;text-align:right}

/* partners */
.partners{position:absolute;left:43px;top:1094px;width:615px;display:flex;justify-content:space-between;align-items:center;font-size:10px;font-weight:600;color:#555}

/* footer */
.site-footer{position:absolute;left:0;top:1134px;width:701px;height:66px;background:var(--footer);color:#c8c8c8}
.footer-nav{position:absolute;left:43px;top:11px;font-size:7.4px}
.footer-nav span{margin:0 5px;color:#888}
.copyright{position:absolute;left:43px;top:33px;font-size:6.6px;line-height:10px}
.copyright b{color:var(--red);font-weight:400}
.connect{position:absolute;left:562px;top:11px;font-size:7.4px}
.social{position:absolute;left:562px;top:28px;display:flex;gap:2px}
.social i{width:18px;height:18px;border-radius:50%;background:var(--white)}
</style>
</head>
<body>

<header class="site-header">
  <div class="brand"><span class="brand-dot"></span><span class="brand-name">ThreadKove</span></div>
  <nav class="main-nav">
    <a href="#">Home</a><a href="#">About Us</a><a href="#">Company</a>
    <a href="#" class="accent">Log In</a><a href="#" class="accent">Register</a>
  </nav>
</header>

<section class="hero" role="img" aria-label="Photo of a smiling group of people seated in a circle, talking together">
  <div class="hero-caption">
    <h1><span>Welcome to</span> ThreadKove</h1>
    <p>Track, Relate, Investigate, <strong>SOLVE</strong></p>
  </div>
  <div class="slider-dots"><i class="on"></i><i></i><i></i><i></i></div>
</section>

<section class="intro">
  <h2 class="section-title">What is ThreadKove?</h2>
  <p class="body-copy">Have you ever compiled a lot of data about something, but been unable to figure out what it means? Often, the number of people involved, the number of events at which they might have met, and the number of common contacts are just too much for a person to track. This can happen when you are trying to understand the players and interests in current events, or the characters and actions in a novel. It’s easy to collect the data, but hard to visualize it or analyze the relationships.</p>
  <p class="body-copy">This is where ThreadKove comes in. ThreadKove allows you to easily visualize people, events, things, groups, and timelines and to easily see the relationships between them. Use ThreadKove to plot a novel, or to investigate a crime. Use it to analyze your favorite conspiracy theory and look for relationships that have eluded the investigators. Use it to track the causes and results of historical events – or current ones. Use it to track changing relationships among your friends at high school. Use it to track the twists and turns of a role-playing game. There’s no end to what you can investigate with ThreadKove.</p>
</section>

<section class="features">
  <article class="feature-card" style="left:43px">
    <svg width="62" height="62" viewBox="0 0 62 62" fill="none" stroke="#fff" stroke-width="4">
      <rect x="3" y="3" width="56" height="56"/>
      <line x1="3" y1="11" x2="59" y2="11"/>
      <rect x="11" y="19" width="40" height="9"/><rect x="11" y="33" width="40" height="9"/><rect x="11" y="47" width="40" height="6"/>
    </svg>
    <h2>Organize</h2>
    <p>ThreadKove is an on-line system that allows you to enter what you know about a person, event, object, or group.</p>
    <span class="learn">LEARN MORE</span>
  </article>
  <article class="feature-card" style="left:254px">
    <svg width="94" height="62" viewBox="0 0 94 62" fill="none" stroke="#fff" stroke-width="4">
      <path d="M3 31 Q47 -12 91 31 Q47 74 3 31 Z"/>
      <circle cx="47" cy="31" r="19"/>
      <path d="M47 18 V31 H57"/>
    </svg>
    <h2>Visualize</h2>
    <p>Once data has been entered, use ThreadKove’s graphical analysis tools to analyze your data in new ways.</p>
    <span class="learn">LEARN MORE</span>
  </article>
  <article class="feature-card" style="left:465px">
    <svg width="66" height="64" viewBox="0 0 66 64" fill="#fff">
      <circle cx="33" cy="6" r="5"/><rect x="26" y="12" width="14" height="15" rx="2"/>
      <circle cx="10" cy="40" r="5"/><rect x="3" y="46" width="14" height="15" rx="2"/>
      <circle cx="56" cy="40" r="5"/><rect x="49" y="46" width="14" height="15" rx="2"/>
      <path d="M31 29h4v8l10 6-2 3-10-6-10 6-2-3 10-6z"/>
    </svg>
    <h2>Colaborate</h2>
    <p>ThreadKove is an on-line system that allows you to enter what you know about a person, event, object, or group.</p>
    <span class="learn">LEARN MORE</span>
  </article>
</section>

<h2 class="section-title how-title">How does ThreadKove work?</h2>
<p class="body-copy how-copy">Once data has been entered, use ThreadKove’s graphical analysis tools to analyze your data in new ways. Use relationship maps to find out how two people or groups are associated. Use timeline analysis to show cause and effect of seemingly unrelated events. Use social network mapping to show how relationships change over time. Look for events that stand out or relationships that have great impact on multiple events. Like a spider’s web, look for the intersections that matter, then look for the players that brought that intersection into focus.</p>
<div class="btn" style="left:43px;top:854px;width:73px">READ MORE</div>
<div class="photo" style="left:386px;top:748px;width:283px;height:120px;background:linear-gradient(90deg,#eeeae4,#d9b48e 45%,#b07a4f 70%,#efe9e2)" role="img" aria-label="Paper cut-out figures seated on small wooden benches in a row"></div>

<div class="get-band"></div>
<div class="photo" style="left:43px;top:911px;width:205px;height:136px;background:linear-gradient(120deg,#6f6a60,#a49a8a 50%,#4c5a6e)" role="img" aria-label="Photo of three students talking together outdoors"></div>
<h2 class="section-title get-title">What do I get with ThreadKove?</h2>
<div class="get-copy">
  <p class="body-copy">Basic ThreadKove will allow any registered user to create, maintain and analyze one investigation. Advanced features will be available a la carte and will include special analytical reports, multiple investigations, and the ability to share an investigation among multiple users. Investigations of general interest could also be shared publicly in read-only mode.</p>
  <p class="body-copy">You will also get access to several read-only public investigations to use as a model. These might include the plots of popular novels or movies, the details of a major political event, or an investigation into a famous crime.</p>
</div>
<div class="btn" style="left:585px;top:1026px;width:73px">READ MORE</div>

<section class="partners" aria-label="Partners">
  <span>Norvane</span><span>Kelmora</span><span>Fennick</span><span>Zorilo</span><span>Plinkett</span><span>Marrow</span><span>Quillion</span><span>Tavo</span><span>Brevix</span><span>Ostrel</span><span>Lumaro</span>
</section>

<footer class="site-footer">
  <nav class="footer-nav">Home<span>|</span>About<span>|</span>Services<span>|</span>FAQs<span>|</span>Contact</nav>
  <p class="copyright">Copyright © 2014. <b>ThreadKove</b><br>All Right Reserved</p>
  <p class="connect">Connect Us:</p>
  <div class="social" aria-label="Social links"><i></i><i></i><i></i><i></i><i></i></div>
</footer>

</body>
</html>
```